Vodka Soda brand identity design and label design

New vodka soda (hard seltzer) brand needs a brand identity design and label designs.

The brand name is VELMO

We produce vodka soda packaged in cans. They come in three flavours
- Raspberry and Lime
- Pina Colada
- Black Cherry

We would like to have the designs look similar (same template) but have one difference depending on the fruit flavour.

The final delivered package should contain
- brand identity design guide with a logo, font and colour schemes
- 3 label designs on the same template (label size 8.125 x 5 inches)

Some example designs of similar products are attached to the project.

Target Market(s)

Gender neutral, younger population

Colors
000000

Requirements
Must have
• Bright background and bright eye catching colours.

```html
<!DOCTYPE html>
<html lang="en">
<head>
<meta charset="utf-8">
<title>VELMO Hard Seltzer – Label Range</title>
<link rel="stylesheet" href="https://fonts.googleapis.com/css2?family=Montserrat:wght@500;600&family=Kaushan+Script&family=Caveat:wght@500&family=Crimson+Text:wght@600&display=swap">
<style>
  :root {
    --ink: #000000;
    --paper: #ffffff;
    --stage: #e9e9e9;
    --grey-text: #6b6b6b;
    --teal: #2cb4c6;
    --red: #e1262b;
    --burgundy: #7b1431;
    --yellow: #f2d01c;
    --lime: #7cc63b;
    --pink-script: #c23a6a;
  }
  * { box-sizing: border-box; margin: 0; padding: 0; }
  html, body { width: 1200px; height: 846px; overflow: hidden; }
  body { background: var(--stage); }
  .range {
    width: 1200px; height: 846px;
    display: flex; justify-content: center; align-items: center; gap: 40px;
  }
  .label {
    position: relative;
    width: 340px; height: 740px;
    background: var(--paper);
    overflow: hidden;
    box-shadow: 0 4px 18px rgba(0,0,0,.12);
    text-align: center;
  }
  .claim {
    position: absolute; top: 40px; left: 0; right: 0;
    font: 600 12px/1 "Montserrat", sans-serif;
    letter-spacing: .04em; color: var(--grey-text);
  }
  .brand-name {
    position: absolute; top: 74px; left: 0; right: 0;
    font: 500 54px/1 "Montserrat", sans-serif;
    color: var(--ink); letter-spacing: .02em;
  }
  .product-type {
    position: absolute; top: 140px; left: 0; right: 0;
    font: 500 31px/1 "Montserrat", sans-serif; color: var(--ink);
  }
  .fruit-art {
    position: absolute; top: 196px; left: 70px;
    width: 200px; height: 170px; border-radius: 50%;
  }
  .descriptor {
    position: absolute; top: 392px; left: 0; right: 0;
    font: 600 13px/1 "Montserrat", sans-serif;
    letter-spacing: .03em; color: var(--grey-text);
  }
  .hint {
    position: absolute; top: 416px; left: 0; right: 0;
    font: 500 26px/1 "Caveat", cursive;
  }
  .flavour-band {
    position: absolute; top: 470px; left: 0; right: 0; bottom: 0;
  }
  .flavour-band svg { position: absolute; left: 0; bottom: 0; }
  .flavour-name {
    position: absolute; top: 70px; left: 0; right: 0;
    font: 400 52px/1.05 "Kaushan Script", cursive;
    color: var(--paper);
  }
  .volume {
    position: absolute; bottom: 70px; left: 0; right: 0;
    font: 600 16px/1 "Crimson Text", serif; color: var(--paper);
  }

  .label--pina .fruit-art { background: radial-gradient(circle at 40% 55%, #f6c92c, #e9a92a 55%, #8a5a35 85%); }
  .label--pina .hint { color: var(--teal); }
  .label--pina .flavour-band { background: var(--teal); }

  .label--rasp .fruit-art { background: radial-gradient(circle at 62% 45%, #b9e25a, #6fbf33 45%, #d9263a 80%); }
  .label--rasp .hint { color: var(--red); }
  .label--rasp .flavour-band { background: var(--red); }
  .label--rasp .flavour-name { top: 52px; font-size: 56px; }

  .label--cherry .fruit-art { background: radial-gradient(circle at 50% 60%, #8c0f1f, #5a0812 55%, #2f7a2a 90%); }
  .label--cherry .hint { color: var(--pink-script); }
  .label--cherry .flavour-band { background: var(--burgundy); }
</style>
</head>
<body>
<main class="range">

  <section class="label label--pina">
    <p class="claim">NATURAL FLAVOURS. NO CARBS.</p>
    <p class="brand-name">VELMO</p>
    <p class="product-type">HARD SELTZER</p>
    <div class="fruit-art" role="img" aria-label="Illustration of pineapple wedges, a halved coconut and a cocktail umbrella"></div>
    <p class="descriptor">ALCOHOLIC SPARKLING WATER</p>
    <p class="hint">whit a hint of</p>
    <div class="flavour-band">
      <p class="flavour-name">Piña Colada</p>
      <p class="volume">5% ALC./VOL. | 473 mL</p>
      <svg width="340" height="60" viewBox="0 0 340 60"><polygon points="0,40 340,8 340,60 0,60" fill="var(--yellow)"/></svg>
    </div>
  </section>

  <section class="label label--rasp">
    <p class="claim">NATURAL FLAVOURS. NO CARBS.</p>
    <p class="brand-name">VELMO</p>
    <p class="product-type">HARD SELTZER</p>
    <div class="fruit-art" role="img" aria-label="Illustration of a raspberry beside a halved lime"></div>
    <p class="descriptor">ALCOHOLIC SPARKLING WATER</p>
    <p class="hint">whit a hint of</p>
    <div class="flavour-band">
      <p class="flavour-name">Raspberry<br>&amp;Lime</p>
      <p class="volume">5% ALC./VOL. | 473 mL</p>
      <svg width="340" height="60" viewBox="0 0 340 60"><polygon points="0,40 340,8 340,60 0,60" fill="var(--lime)"/></svg>
    </div>
  </section>

  <section class="label label--cherry">
    <p class="claim">NATURAL FLAVOURS. NO CARBS.</p>
    <p class="brand-name">VELMO</p>
    <p class="product-type">HARD SELTZER</p>
    <div class="fruit-art" role="img" aria-label="Illustration of a pair of dark cherries on a stem with a leaf"></div>
    <p class="descriptor">ALCOHOLIC SPARKLING WATER</p>
    <p class="hint">whit a hint of</p>
    <div class="flavour-band">
      <p class="flavour-name">Black Cherry</p>
      <p class="volume">5% ALC./VOL. | 473 mL</p>
      <svg width="340" height="60" viewBox="0 0 340 60"><polygon points="0,40 340,8 340,60 0,60" fill="var(--yellow)"/></svg>
    </div>
  </section>

</main>
</body>
</html>
```